Business card design and logo needed please help

I need a card for a new plumbing business. i want double sided gloss and on the front i need an attractive logo for my business the incorperates a rhino and plumbing to go with my name aswell as my contact info. logo aswell has to be not out there but remeberable as it will be representing this later to be large Business.Could also incorperate the initials of my buisness being TWB. On the back i want the type of work that i undertake, Plumbing, Maintaince, gasfitting and certification, sanitary drainage and stormwater, drain cleaning, All hot water systems installations and repair , FREE QUOTE is needed to stand out aswell. i like an indate colour design but more then one colour like black and grey or anything.info has to be easy to read that will draw in all types of clients. want a slogan on it saying "tough on Quality" aswell. Email aswell has changed to make it easier for people. Its now( Twbadvisory@keltomail.com)
Industry/Entity Type
Business
Contact Information for Business Card
Tolbek's Plumbing and Gas Fitting, Colin Marsdale, QBSA No. 47 80 916, ABN No. 58 204 917 346, Email. Tolbeksplumbingandgasfitting@keltomail.com, Mobile no. 0468 915 304
Logo styles of interest
Pictorial/Combination Logo
Abstract Logo
Character Logo
Look and feel

```html
<!DOCTYPE html>
<html lang="en">
<head>
<meta charset="utf-8">
<title>Tolbek's Plumbing and Gas Fitting – Business Card</title>
<link rel="stylesheet" href="https://fonts.googleapis.com/css2?family=Sintony:wght@400;700&family=Alegreya+Sans:ital,wght@0,500;0,700;1,500&family=Roboto:wght@700&display=swap">
<style>
  :root {
    --brand-blue: #38aac9;
    --ink: #0b0b0b;
    --paper: #ffffff;
  }
  html, body {
    margin: 0;
    padding: 0;
    overflow: hidden;
    background: var(--paper);
  }
  .card {
    position: relative;
    width: 1200px;
    height: 741px;
    background: var(--paper);
    overflow: hidden;
  }
  .side-panel {
    position: absolute;
    left: 0;
    top: 0;
    width: 481px;
    height: 741px;
    background: var(--brand-blue);
    color: var(--paper);
  }
  .business-name {
    position: absolute;
    left: 0;
    top: 56px;
    width: 481px;
    margin: 0;
    text-align: center;
    font-family: "Sintony", sans-serif;
    font-weight: 400;
    font-size: 50px;
    line-height: 76px;
    letter-spacing: 0.5px;
  }
  .registrations {
    position: absolute;
    left: 36px;
    top: 444px;
    margin: 0;
    font-family: "Alegreya Sans", sans-serif;
    font-weight: 500;
    font-size: 45px;
    line-height: 44px;
    white-space: nowrap;
  }
  .mobile {
    position: absolute;
    left: 36px;
    top: 556px;
    margin: 0;
    font-family: "Roboto", sans-serif;
    font-weight: 700;
    font-size: 56px;
    line-height: 54px;
    white-space: nowrap;
  }
  .brand {
    position: absolute;
    left: 880px;
    top: 50px;
    width: 220px;
    display: flex;
    flex-direction: column;
    align-items: center;
  }
  .brand-dot {
    width: 140px;
    height: 140px;
    border-radius: 50%;
    background: var(--brand-blue);
  }
  .brand-name {
    margin: 20px 0 0;
    font-family: "Sintony", sans-serif;
    font-weight: 400;
    font-size: 84px;
    line-height: 90px;
    color: var(--ink);
  }
  .owner-name {
    position: absolute;
    left: 481px;
    right: 0;
    top: 340px;
    margin: 0;
    text-align: center;
    font-family: "Sintony", sans-serif;
    font-weight: 400;
    font-size: 82px;
    line-height: 90px;
    color: var(--ink);
    white-space: nowrap;
  }
  .slogan {
    position: absolute;
    left: 481px;
    right: 0;
    top: 432px;
    margin: 0;
    text-align: center;
    font-family: "Alegreya Sans", sans-serif;
    font-style: italic;
    font-weight: 500;
    font-size: 74px;
    line-height: 80px;
    color: var(--brand-blue);
    white-space: nowrap;
  }
  .email {
    position: absolute;
    left: 516px;
    top: 624px;
    margin: 0;
    font-family: "Alegreya Sans", sans-serif;
    font-weight: 700;
    font-size: 44px;
    line-height: 50px;
    color: var(--brand-blue);
    white-space: nowrap;
  }
</style>
</head>
<body>
  <main class="card">
    <section class="side-panel">
      <h1 class="business-name">Tolbek's<br>Plumbing and<br>Gas Fitting</h1>
      <p class="registrations">QBSA No. 47 80 916<br>ABN No. 58 204 917 346</p>
      <p class="mobile">Mobile no.<br>0468 915 304</p>
    </section>
    <div class="brand" role="img" aria-label="TWB business logo">
      <div class="brand-dot"></div>
      <p class="brand-name">TWB</p>
    </div>
    <h2 class="owner-name">Colin Marsdale</h2>
    <p class="slogan">"Tough On Quality"</p>
    <p class="email">Email:&nbsp; Twbadvisory@keltomail.com</p>
  </main>
</body>
</html>
```